Colm Vestry Personal Website Yoga Teacher and Personal Fitness Trainer

Let's pick a SITEFORGE theme that can work with Video Bckground. I would like a website design to look like some of nice Pagewright themes.
I would like to have a Video background of me teaching. I can provide video. Please view my current Siteforge site: www.colmvestry-example.com. I also have new logo. See file cves1.png

Project Deadline Extended
Reason: I am guaranteeing this project because i believe designers can deliver. I am extending 5 days because the homepage image/video slider is intricate and takes a bit of time. I have provided details, images, video etc. in Filecrate. Tx

Target Market(s)

All people needing & wanting personal help (they can trust and feel safe and nurtured) for their health (wellness, nutrition, fitness, exercise). And people wanting extraordinary yoga teaching.

Industry/Entity Type

Fitness

Number of Pages Required

5+ page

Colors
9bcb3b
add136
cadf82
eaf2ce

Requirements
Must have
• Template that can use a video background
Nice to have
• Need to show good image gallery and testimonial videos

```html
<!DOCTYPE html>
<html lang="en">
<head>
<meta charset="utf-8">
<title>Colm Vestry – Yoga Teacher &amp; Personal Fitness Trainer</title>
<link href="https://fonts.googleapis.com/css2?family=Raleway:wght@400;500;600;700&family=Open+Sans:ital,wght@0,400;0,600;0,700;1,400&display=swap" rel="stylesheet">
<style>
:root{
  --green:#9bcb3b;
  --green-title:#8fc23a;
  --green-light:#cadf82;
  --green-pale:#eaf2ce;
  --header-bg:#eef4da;
  --footer-bg:#8ebd3a;
  --text:#333;
  --rule:#cfcfcf;
  --dark-btn:#3a3a3a;
  --leaf:#5e9b2a;
}
*{box-sizing:border-box;margin:0;padding:0}
html,body{width:1200px;height:2187px;overflow:hidden;background:#fff}
body{position:relative;font-family:"Open Sans",sans-serif;color:var(--text)}

/* header */
.site-header{position:absolute;left:0;top:0;width:1200px;height:106px;background:var(--header-bg)}
.brand{position:absolute;left:104px;top:26px;display:flex;align-items:center;gap:10px}
.brand-mark{width:34px;height:34px;border-radius:50%;background:var(--green)}
.brand-name{font-family:"Raleway",sans-serif;font-weight:700;font-size:23px;color:#4f7d1f;line-height:1}
.brand-tag{font-family:"Raleway",sans-serif;font-size:10px;color:#6f9b2c;margin-top:4px}
.main-nav a{position:absolute;top:0;height:106px;line-height:114px;font-family:"Raleway",sans-serif;font-size:12.5px;color:#6a8a3a;text-decoration:none;transform:translateX(-50%);white-space:nowrap}
.main-nav a.active{background:var(--green-light);width:126px;text-align:center;transform:none;color:#fff}
.main-nav a.active::after{content:"";position:absolute;left:55px;bottom:-8px;border:8px solid transparent;border-bottom:0;border-top-color:var(--green-light)}

/* hero */
.hero{position:absolute;left:0;top:106px;width:1200px;height:552px;
  background:linear-gradient(90deg,rgba(0,0,0,.18) 0%,rgba(0,0,0,0) 50%),
  linear-gradient(90deg,#2f5a1c 0%,#44742a 35%,#6f7e4a 55%,#a7988a 72%,#d9d6d0 100%)}
.hero-title{position:absolute;left:98px;top:201px;font-family:"Raleway",sans-serif;font-weight:700;font-size:22.5px;color:#fff}
.hero-text{position:absolute;left:98px;top:243px;width:474px;font-family:"Raleway",sans-serif;font-size:12.5px;line-height:20.5px;color:#fff;text-align:justify}
.hero-btn{position:absolute;top:342px;height:37px;line-height:37px;padding:0 13px;font-family:"Raleway",sans-serif;font-weight:700;font-size:12px;color:#fff;border-radius:2px}
.btn-green{background:var(--green)}
.btn-dark{background:var(--dark-btn)}
.play{position:absolute;width:64px;height:64px;border-radius:50%;background:rgba(20,20,20,.8)}
.play::after{content:"";position:absolute;left:26px;top:21px;border:11px solid transparent;border-right:0;border-left:14px solid #fff}
.dots{position:absolute;left:580px;top:520px;display:flex;gap:8px}
.dots span{width:7px;height:7px;border-radius:50%;background:rgba(255,255,255,.35)}
.dots span.on{background:rgba(255,255,255,.75)}

/* sections */
.section-title{position:absolute;left:0;width:1200px;text-align:center;font-family:"Raleway",sans-serif;font-weight:400;font-size:20px;color:var(--green-title);letter-spacing:.3px}
.divider{position:absolute;left:100px;width:1001px;height:30px}
.divider::before{content:"";position:absolute;left:0;right:0;top:15px;border-top:1px solid var(--rule)}
.divider .mark{position:absolute;left:486px;top:0;width:30px;height:30px;background:#fff}
.divider .mark i{position:absolute;border-radius:50%;background:var(--leaf)}
.sep{position:absolute;left:0;width:1200px;height:4px;border-top:1px solid #ddd;border-bottom:1px solid #ddd}
.read-more{position:absolute;height:27px;line-height:27px;padding:0 9px;background:linear-gradient(#a9d24c,#8fbf30);color:#fff;font-family:"Raleway",sans-serif;font-weight:700;font-size:11.5px;border-radius:2px}
.welcome-text{position:absolute;left:186px;top:772px;width:828px;font-size:12px;line-height:18.5px;text-align:center;color:var(--text)}

/* services */
.accordion{position:absolute;left:111px;top:1039px;width:612px}
.acc-head{position:relative;border-top:1px solid var(--rule);padding:9px 0 8px;font-family:"Raleway",sans-serif;font-size:17px;color:var(--green-title)}
.acc-toggle{position:absolute;right:10px;top:13px;width:17px;height:17px;border-radius:50%;background:#e2e2e2}
.acc-toggle::after{content:"";position:absolute;left:5px;top:7px;border:3.5px solid transparent;border-bottom:0;border-top-color:#777}
.acc-toggle.closed::after{left:7px;top:5px;border:3.5px solid transparent;border-right:0;border-left-color:#777}
.acc-body{padding:4px 0 9px}
.acc-body h3{font-family:"Raleway",sans-serif;font-weight:500;font-size:16px;color:#111;margin-bottom:3px}
.acc-body p{font-family:"Raleway",sans-serif;font-size:10.8px;line-height:18.5px;color:#222}
.acc-last{border-bottom:1px solid var(--rule)}
.framed{position:absolute;background:#fff;border:1px solid #ddd;padding:4px;box-shadow:0 1px 2px rgba(0,0,0,.08)}
.framed .fill{width:100%;height:100%}

/* gallery */
.arrow{position:absolute;width:22px;height:22px;border-radius:50%;background:#e3e3e3}
.arrow::after{content:"";position:absolute;top:7px;border:4px solid transparent}
.arrow.prev::after{left:6px;border-left:0;border-right:6px solid #777}
.arrow.next::after{left:9px;border-right:0;border-left:6px solid #777}

/* testimonials */
.video-card{position:absolute;top:1709px;width:319px}
.video-card .framed{position:relative;height:172px}
.video-card .play{width:34px;height:34px;top:50%;margin-top:-17px}
.video-card .play::after{left:13px;top:10px;border-width:7px;border-left-width:9px}
.video-card p{margin-top:10px;font-style:italic;font-size:11px;line-height:18px;color:#333;text-align:justify}
.video-card .read-more{position:relative;display:inline-block;margin-top:11px}
.card-label{position:absolute;font-family:"Raleway",sans-serif;font-weight:700;font-size:19px;color:#7aa83a;white-space:nowrap}

/* footer */
.site-footer{position:absolute;left:0;top:2012px;width:1200px;height:175px;background:var(--footer-bg)}
.foot-nav{position:absolute;top:35px;width:1200px;display:flex;justify-content:center;gap:29px;font-family:"Raleway",sans-serif;font-size:12.5px;color:#fff}
.social{position:absolute;top:73px;left:512px;display:flex;gap:12px}
.social a{position:relative;width:35px;height:35px;border-radius:50%;background:#fff;overflow:hidden}
.social a span{position:absolute;width:1px;height:1px;overflow:hidden;clip:rect(0 0 0 0)}
.copyright{position:absolute;top:136px;width:1200px;text-align:center;font-family:"Raleway",sans-serif;font-size:11.5px;color:#fff}
</style>
</head>
<body>

<header class="site-header">
  <div class="brand">
    <span class="brand-mark"></span>
    <div><div class="brand-name">COLM VESTRY</div><div class="brand-tag">Expert Guidance for a Healthier Life</div></div>
  </div>
  <nav class="main-nav">
    <a style="left:405px">HOME</a>
    <a style="left:510px">ABOUT COLM</a>
    <a style="left:626px">SCHEDULE</a>
    <a class="active" style="left:666px">SERVICES</a>
    <a style="left:853px">CLIENTS</a>
    <a style="left:959px">GALLERY</a>
    <a style="left:1069px">CONTACT</a>
  </nav>
</header>

<section class="hero" role="img" aria-label="Video background: portrait of the yoga teacher in a white shirt against green foliage">
  <h1 class="hero-title">LEADER OF YOGA TEACHER TRAININGS</h1>
  <p class="hero-text">Are you at a decision point in your life, where wellness has become a priority and you are seeking additional support to reach your goals? Bend in the Path Wellness offers a unique, exciting innovation in wellness and nutrition: health coaching. As a Certified Health Coach, I...</p>
  <span class="hero-btn btn-green" style="left:98px">TEACHER OF YOGA</span>
  <span class="hero-btn btn-dark" style="left:254px">PERSONAL FITNESS TRAINER</span>
  <span class="play" style="left:567px;top:289px"></span>
  <div class="dots"><span class="on"></span><span class="on"></span><span class="on"></span><span></span></div>
</section>

<h2 class="section-title" style="top:684px">WELCOME TO OUR WEBSITE</h2>
<div class="divider" style="top:730px"><span class="mark"><i style="left:13px;top:6px;width:4px;height:18px;border-radius:2px"></i><i style="left:2px;top:13px;width:5px;height:5px"></i><i style="left:23px;top:13px;width:5px;height:5px"></i></span></div>
<p class="welcome-text">Are you at a decision point in your life, where wellness has become a priority and you are seeking additional support to reach your goals? Colm offers his unique experience to help inspire you to become healthier. He will guide you to wellness by working with you to create a custom tailored plan based on your needs and what you really want to achieve. Whether it is yoga you seek, improved nutrition, coaching, mindfulness &amp; meditation or increased fitness, Colm has the experience, skills and personality to get you there. Please take a moment to read the fabulous testimonials (and see the video testimonials) Colm has received from so many of his yoga students and fitness clients.</p>
<span class="read-more" style="left:556px;top:872px">READ MORE</span>
<div class="sep" style="top:911px"></div>

<h2 class="section-title" style="top:942px">STATE SERVICES</h2>
<div class="divider" style="top:987px"><span class="mark"><i style="left:13px;top:6px;width:4px;height:18px;border-radius:2px"></i><i style="left:2px;top:13px;width:5px;height:5px"></i><i style="left:23px;top:13px;width:5px;height:5px"></i></span></div>
<div class="accordion">
  <div class="acc-head">EXPERT GUIDANCE FOR A HEALTHIER LIFE<span class="acc-toggle"></span></div>
  <div class="acc-body">
    <h3>YOGA, WELLNESS &amp; FITNESS with COLM VESTRYThe Natural Way</h3>
    <p>Colm Vestry's personal fitness &amp; yoga training, yoga classes, workshops &amp; retreats, ayurveda/shamanic lifestyle teaching, diet &amp; nutrition coaching, guided meditation, specialty senior classes and yoga teacher training programs are offered with one purpose in mind: to help you live a better, happier and healthier life! Awaken your potential. Exercise, get a fitter body, learn yoga, calm your mind, relax &amp; reduce stress and experience vitality &amp; inner peace. Why wait? Begin practicing today. Start your new journey to true wellness now.</p>
  </div>
  <div class="acc-head acc-last">EXPERT LEADER OF YOGA TEACHER TRAINING<span class="acc-toggle closed"></span></div>
</div>
<div class="framed" style="left:763px;top:1035px;width:331px;height:218px"><div class="fill" role="img" aria-label="Photo: teacher seated in a yoga twist on a mat in a bright studio" style="background:linear-gradient(180deg,#f1e3cb 0%,#e4c7a0 55%,#a97a52 80%,#6a5446 100%)"></div></div>

<h2 class="section-title" style="top:1285px">GALLERY</h2>
<div class="divider" style="top:1330px"><span class="mark"><i style="left:13px;top:6px;width:4px;height:18px;border-radius:2px"></i><i style="left:2px;top:13px;width:5px;height:5px"></i><i style="left:23px;top:13px;width:5px;height:5px"></i></span></div>
<span class="arrow prev" style="left:109px;top:1437px"></span>
<div class="framed" style="left:158px;top:1373px;width:212px;height:158px"><div class="fill" role="img" aria-label="Gallery photo: personal training session outdoors among plants" style="background:linear-gradient(180deg,#3b5a2c 0%,#4a6234 60%,#3c3a30 100%)"></div></div>
<div class="framed" style="left:383px;top:1373px;width:212px;height:158px"><div class="fill" role="img" aria-label="Gallery photo: group yoga class in a studio" style="background:linear-gradient(180deg,#e0d6c6 0%,#c8a88a 55%,#a0522d 100%)"></div></div>
<div class="framed" style="left:607px;top:1373px;width:212px;height:158px"><div class="fill" role="img" aria-label="Gallery photo: students in standing yoga poses" style="background:linear-gradient(180deg,#e6ddd0 0%,#b7a897 60%,#6a5e54 100%)"></div></div>
<div class="framed" style="left:831px;top:1373px;width:212px;height:158px"><div class="fill" role="img" aria-label="Gallery photo: triangle pose on a mat by bright curtains" style="background:linear-gradient(180deg,#f1e6d2 0%,#ebdcc4 70%,#a8916f 100%)"></div></div>
<span class="arrow next" style="left:1059px;top:1437px"></span>
<div class="sep" style="top:1570px"></div>

<h2 class="section-title" style="top:1603px">VIDEO TESTIMONIALS</h2>
<div class="divider" style="top:1647px"><span class="mark"><i style="left:13px;top:6px;width:4px;height:18px;border-radius:2px"></i><i style="left:2px;top:13px;width:5px;height:5px"></i><i style="left:23px;top:13px;width:5px;height:5px"></i></span></div>

<div class="video-card" style="left:98px">
  <div class="framed" style="width:319px"><div class="fill" role="img" aria-label="Video thumbnail: teacher in white seated in meditation" style="background:#f3f2ee"></div><span class="play" style="left:134px"></span><span class="card-label" style="left:174px;top:74px">COLM VESTRY</span></div>
  <p>Nemo enim ipsam voluptatem quia voluptas sit aspernatur aut odit aut fugit, sed quia consequuntur magni dolores eos qui ratione voluptatem sequi nesciunt.</p>
  <span class="read-more">READ MORE</span>
</div>
<div class="video-card" style="left:441px">
  <div class="framed" style="width:319px"><div class="fill" role="img" aria-label="Video thumbnail: brand title card on a soft blue-violet background" style="background:linear-gradient(180deg,#e6e7f3,#d4d6ea)"></div><span class="play" style="left:142px"></span></div>
  <p>Nemo enim ipsam voluptatem quia voluptas sit aspernatur aut odit aut fugit, sed quia consequuntur magni dolores eos qui ratione voluptatem sequi nesciunt.</p>
  <span class="read-more">READ MORE</span>
</div>
<div class="video-card" style="left:784px">
  <div class="framed" style="width:319px"><div class="fill" role="img" aria-label="Video thumbnail: black and white photo of the teacher beside a tree" style="background:linear-gradient(180deg,#6a6a66,#4a4a46)"></div><span class="play" style="left:142px"></span></div>
  <p>Nemo enim ipsam voluptatem quia voluptas sit aspernatur aut odit aut fugit, sed quia consequuntur magni dolores eos qui ratione voluptatem sequi nesciunt.</p>
  <span class="read-more">READ MORE</span>
</div>

<footer class="site-footer">
  <nav class="foot-nav"><span>HOME</span><span>ABOUT US</span><span>BLOG</span><span>CLIENTS</span><span>CONTACT</span><span>MEDIA »</span><span>NUTRITION</span><span>SCHEDULE/CLASSES</span><span>SERVICES</span></nav>
  <div class="social">
    <a aria-label="Share"><span>Share</span></a>
    <a aria-label="Post"><span>Post</span></a>
    <a aria-label="Link"><span>Link</span></a>
    <a aria-label="Feed"><span>Feed</span></a>
  </div>
  <div class="copyright">2015 © www.companyname.com</div>
</footer>

</body>
</html>
```